Yorvane crafters

Vesk T620 year 2021 needs a full wrap. My companies name is Yorvane Crafters we are a high end landscape design build company. We specialize in pavers retaining walls, patio covers and decks.

```html
<!DOCTYPE html>
<html lang="en">
<head>
<meta charset="utf-8">
<title>Yorvane Crafters – Truck Wrap</title>
<link rel="stylesheet" href="https://fonts.googleapis.com/css2?family=Poppins:wght@500;700&family=Cinzel:wght@500&display=swap">
<style>
  :root {
    --navy: #22394a;
    --navy-deep: #182a37;
    --gold: #f2c230;
    --white: #ffffff;
    --glass: #3a4148;
    --tire: #1c1d1f;
    --rim: #9aa0a6;
    --light: #b3202a;
    --page: #ffffff;
  }
  * { margin: 0; padding: 0; box-sizing: border-box; }
  html, body { width: 1200px; height: 645px; overflow: hidden; background: var(--page); }
  .wrap-canvas { position: relative; width: 1200px; height: 645px; font-family: "Poppins", sans-serif; }
  .truck-art { position: absolute; inset: 0; }

  .contact-icons { position: absolute; left: 168px; top: 292px; display: flex; gap: 14px; align-items: center; }
  .contact-icons .icon { width: 24px; height: 24px; border-radius: 5px; background: var(--navy); display: flex; align-items: center; justify-content: center; }
  .contact-icons .divider { width: 1px; height: 18px; background: var(--navy); opacity: .5; }

  .phone { position: absolute; left: 110px; top: 318px; font-weight: 700; font-size: 32px; line-height: 40px; color: var(--navy); letter-spacing: .3px; white-space: nowrap; }
  .email { position: absolute; left: 112px; top: 362px; font-weight: 700; font-size: 13.5px; line-height: 16px; color: var(--navy); white-space: nowrap; }
  .address { position: absolute; left: 112px; top: 380px; font-weight: 500; font-size: 10.5px; line-height: 13px; color: var(--navy); white-space: nowrap; }

  .brand { position: absolute; left: 402px; top: 290px; width: 214px; text-align: center; color: var(--navy); }
  .brand .mark { width: 40px; height: 40px; background: var(--navy); margin: 0 auto 12px; }
  .brand .name { font-family: "Cinzel", serif; font-weight: 500; font-size: 17px; line-height: 22px; white-space: nowrap; }
  .brand .tag { font-weight: 500; font-size: 8.5px; letter-spacing: .4px; margin-top: 2px; white-space: nowrap; }

  .services { position: absolute; left: 700px; top: 298px; display: grid; grid-template-columns: repeat(4, auto); justify-content: start; gap: 10px 16px; }
  .service { display: flex; align-items: center; gap: 6px; color: var(--white); font-weight: 700; font-size: 10.5px; line-height: 1.05; text-transform: uppercase; white-space: nowrap; }
  .service .bullet { flex: none; width: 18px; height: 18px; border-radius: 5px; background: var(--gold); display: flex; align-items: center; justify-content: center; }
  .service .bullet::after { content: ""; width: 6px; height: 6px; border-radius: 50%; background: var(--navy); }

  .tagline { position: absolute; left: 1008px; top: 392px; width: 124px; color: var(--navy); text-align: right; }
  .tagline .lead { font-weight: 500; font-size: 8.5px; }
  .tagline .big { font-weight: 700; font-size: 21px; line-height: 1; }
</style>
</head>
<body>
<div class="wrap-canvas">
  <svg class="truck-art" viewBox="0 0 1200 645" xmlns="http://www.w3.org/2000/svg">
    <defs>
      <clipPath id="body-shape">
        <path d="M70,272 Q75,246 110,242 L330,228 L400,150 Q410,142 430,142 L650,140 Q665,142 668,157 L675,285 L1125,285 Q1135,287 1135,300 L1135,455 L985,455 A80,80 0 0 0 825,455 L318,455 A70,70 0 0 0 182,455 L70,455 Z"/>
      </clipPath>
      <linearGradient id="glass-sheen" x1="0" y1="0" x2="1" y2="1">
        <stop offset="0" stop-color="#e9ecef"/>
        <stop offset="1" stop-color="#8d959c"/>
      </linearGradient>
    </defs>

    <g class="body-panels" clip-path="url(#body-shape)">
      <rect class="panel-navy" x="60" y="130" width="1090" height="340" fill="var(--navy)"/>
      <path class="panel-white" d="M60,232 L610,228 C625,300 650,380 665,470 L60,470 Z" fill="var(--white)"/>
      <path class="edge-stripe" d="M610,228 C625,300 650,380 665,470" fill="none" stroke="var(--gold)" stroke-width="14"/>
      <path class="hood-swoosh" d="M60,286 C200,260 330,296 430,276 C480,266 500,250 520,232" fill="none" stroke="var(--gold)" stroke-width="9"/>
      <path class="roof-accent" d="M460,130 L490,130 L480,150 L450,150 Z" fill="var(--gold)"/>
      <rect class="grass-band" x="60" y="428" width="610" height="30" fill="var(--navy)" role="img" aria-label="Grass silhouette border"/>
      <rect class="bed-band" x="676" y="440" width="470" height="20" fill="var(--gold)"/>
      <rect class="bed-dash" x="1005" y="372" width="130" height="68" fill="var(--gold)"/>
      <g class="bed-stripes" fill="var(--gold)">
        <rect x="690" y="418" width="40" height="10"/>
        <rect x="740" y="418" width="40" height="10"/>
        <path d="M1040,364 L1054,364 L1062,338 L1048,338 Z"/>
        <path d="M1068,364 L1082,364 L1090,338 L1076,338 Z"/>
        <path d="M1096,364 L1110,364 L1118,338 L1104,338 Z"/>
      </g>
    </g>

    <g class="windows">
      <path d="M345,228 L410,160 L510,158 L512,228 Z" fill="url(#glass-sheen)"/>
      <path d="M525,158 L640,155 L650,228 L525,228 Z" fill="url(#glass-sheen)"/>
      <path d="M345,228 L410,160 L510,158 L512,228 Z M525,158 L640,155 L650,228 L525,228 Z" fill="none" stroke="var(--glass)" stroke-width="5"/>
    </g>

    <g class="door-lines" fill="none" stroke="var(--navy-deep)" stroke-opacity=".35" stroke-width="1.5">
      <path d="M392,232 L392,428"/>
      <path d="M675,160 L680,455"/>
    </g>

    <g class="wheels">
      <circle cx="250" cy="478" r="62" fill="var(--tire)"/>
      <circle cx="250" cy="478" r="34" fill="var(--rim)"/>
      <circle cx="250" cy="478" r="11" fill="var(--tire)"/>
      <circle cx="905" cy="470" r="70" fill="var(--tire)"/>
      <circle cx="905" cy="470" r="40" fill="var(--rim)"/>
      <circle cx="905" cy="470" r="13" fill="var(--tire)"/>
    </g>
    <rect class="bumper" x="1120" y="430" width="24" height="36" rx="3" fill="var(--tire)"/>
    <rect class="taillight" x="1127" y="300" width="10" height="34" rx="2" fill="var(--light)"/>
  </svg>

  <div class="contact-icons">
    <span class="icon"><svg width="14" height="14" viewBox="0 0 24 24"><path fill="#fff" d="M6.6 10.8a15 15 0 0 0 6.6 6.6l2.2-2.2c.3-.3.7-.4 1-.2 1.1.4 2.3.6 3.6.6.6 0 1 .4 1 1V20c0 .6-.4 1-1 1A17 17 0 0 1 3 4c0-.6.4-1 1-1h3.5c.6 0 1 .4 1 1 0 1.3.2 2.5.6 3.6.1.3 0 .7-.2 1z"/></svg></span>
    <span class="divider"></span>
    <span class="icon"><svg width="14" height="14" viewBox="0 0 24 24"><path fill="none" stroke="#fff" stroke-width="2" d="M3 6h18v12H3z M3 6l9 7 9-7"/></svg></span>
    <span class="divider"></span>
    <span class="icon"><svg width="14" height="14" viewBox="0 0 24 24"><path fill="#fff" d="M12 2a7 7 0 0 0-7 7c0 5 7 13 7 13s7-8 7-13a7 7 0 0 0-7-7zm0 9.5A2.5 2.5 0 1 1 12 6.5a2.5 2.5 0 0 1 0 5z"/></svg></span>
  </div>

  <div class="phone">(555) 014-2290</div>
  <div class="email">INFO@YORVANECRAFTERS.COM</div>
  <div class="address">1180 ALDER RIDGE RD, FENMOOR, WA 98000</div>

  <div class="brand">
    <div class="mark"></div>
    <div class="name">YORVANE CRAFTERS</div>
    <div class="tag">OUTDOOR LIVING SPACES</div>
  </div>

  <div class="services">
    <div class="service"><span class="bullet"></span>Paver<br>Patios</div>
    <div class="service"><span class="bullet"></span>Paver<br>Driveways</div>
    <div class="service"><span class="bullet"></span>Decks &amp;<br>Railings</div>
    <div class="service"><span class="bullet"></span>Pools</div>
    <div class="service"><span class="bullet"></span>Retaining<br>Walls</div>
    <div class="service"><span class="bullet"></span>Firepits &amp;<br>Fireplaces</div>
  </div>

  <div class="tagline">
    <div class="lead">It's Time to Discover</div>
    <div class="big">YOUR ZEN</div>
  </div>
</div>
</body>
</html>
```